2 Page Brochure - Commercial Roofing Company

We are looking for a double sided brochure, full color, for our commercial roofing company that tells customers a little bit about the company, what we do, and shows a few pictures.
The brochure would need to have our logo and color scheme that coordinates with that logo.
I have uploaded our logo, some ideas I had, and then the idea list also has our website on there if you'd like to take a look around there for some more ideas.
I have also uploaded some photos we'd like to use.
Page size should be 8.5" x 11".
Target Market(s)
Commercial Property Owners
Other font styles liked:
- Match logo font ideally so it's cohesive, but whatever looks best
Look and feel

```html
<!DOCTYPE html>
<html lang="en">
<head>
<meta charset="utf-8">
<title>Mesa Ridge Roofing – Two Page Brochure</title>
<link rel="stylesheet" href="https://fonts.googleapis.com/css2?family=Poppins:ital,wght@0,300;0,400;0,500;0,600;0,700;1,500;1,600&family=Oswald:wght@500&display=swap">
<style>
  :root{
    --orange:#e8541f;
    --dark:#222222;
    --dark-2:#1b1b1b;
    --white:#ffffff;
    --gold:#c9a85a;
    --stage-top:#7d7d7d;
    --stage-bottom:#050505;
  }
  *{margin:0;padding:0;box-sizing:border-box}
  html,body{width:1200px;height:789px;overflow:hidden}
  body{
    position:relative;
    background:linear-gradient(to bottom,var(--stage-top) 0%,#5a5a5a 45%,var(--stage-bottom) 100%);
    font-family:"Poppins",sans-serif;color:var(--white);
  }
  .page{position:absolute;top:88px;width:474px;height:613px;background:var(--dark);overflow:hidden}
  .page--front{left:89px}
  .page--back{left:637px}
  .top-bar{position:absolute;left:0;top:0;width:100%;height:5px;background:var(--orange)}

  .brand{position:absolute;left:10px;top:28px;width:150px;display:flex;align-items:center;gap:7px}
  .brand__mark{width:14px;height:14px;background:var(--orange);flex:none}
  .brand__name{font-weight:700;font-size:17px;line-height:1.05;color:var(--white);text-transform:uppercase}
  .badge{position:absolute;left:368px;top:13px;width:61px;height:61px;border:2px solid var(--gold)}

  /* front photo band */
  .photo{position:absolute}
  .photo--facade{left:0;top:83px;width:235px;height:199px;
    background:linear-gradient(180deg,#3f78c4 0%,#8fb1d8 35%,#d9dde2 55%,#5d8a7e 75%,#3a6a5e 100%);
    clip-path:polygon(0 0,100% 0,70% 100%,0 100%)}
  .photo--aerial{left:307px;top:83px;width:167px;height:199px;
    background:linear-gradient(160deg,#6b5a45 0%,#e9ecee 35%,#f4f5f6 60%,#a98a62 85%,#7a6a55 100%);
    clip-path:polygon(30% 0,100% 0,100% 100%,0 100%)}
  .accent-line{position:absolute;height:1.5px;background:var(--orange)}
  .accent-dash{position:absolute;height:0;border-top:1.5px dashed var(--orange)}
  .intro{position:absolute;left:190px;top:114px;width:130px;font-size:10.4px;line-height:12.1px;text-align:center;font-weight:400}
  .hl{color:var(--orange)}

  .specialty{position:absolute;left:8px;top:292px;font-family:"Poppins",sans-serif;font-weight:600;font-size:26px;line-height:27px;letter-spacing:.3px;text-transform:uppercase}
  .specialty .outline{color:transparent;-webkit-text-stroke:1px var(--white)}
  .specialty .solid{color:var(--orange);font-weight:700}
  .body-text{position:absolute;left:8px;width:232px;font-size:11px;line-height:14.6px}
  .body-text--lead{top:381px}
  .body-text--call{top:454px;color:var(--orange)}
  .body-text--small{top:479px;font-size:9.3px;line-height:11.2px;width:226px}
  .photo--store{left:245px;top:298px;width:222px;height:232px;
    background:linear-gradient(180deg,#c4d3e2 0%,#eef1f4 30%,#3c3c3c 45%,#6a4b3c 70%,#b7b7b2 85%,#8d8d88 100%);
    border-bottom-left-radius:30px}
  .store-bar{position:absolute;left:251px;top:300px;width:211px;height:17px;background:var(--orange);opacity:.9}

  .footer-shape{position:absolute;left:0;top:540px;width:474px;height:73px}
  .phone{position:absolute;left:16px;top:572px;font-family:"Oswald",sans-serif;font-weight:500;font-size:30px;line-height:36px;color:var(--dark)}
  .contact{position:absolute;right:16px;top:545px;text-align:right;color:var(--dark);font-weight:600;font-size:12px;line-height:15px}
  .contact__licence{font-weight:700;font-size:14.5px;line-height:18px}

  /* back */
  .photo--backdrop{left:0;top:83px;width:474px;height:485px;
    background:linear-gradient(180deg,#3a4a66 0%,#8a4b3a 20%,#8b6b55 35%,#5a5650 55%,#2e2e2e 75%,#4a3a30 100%)}
  .state-band{position:absolute;left:0;top:83px;width:474px;height:44px;background:linear-gradient(90deg,rgba(34,34,34,.55),rgba(50,70,100,.35))}
  .state-band p{font-style:italic;font-weight:600;font-size:16px;text-align:center;line-height:44px}
  .cert-band{position:absolute;left:0;top:127px;width:474px;height:98px;background:rgba(90,16,10,.78);padding:14px 14px 0}
  .cert-band p{font-weight:600;font-size:12.3px;line-height:15px}
  .cert-band strong{font-size:14.5px;font-weight:600}
  .makers{display:flex;gap:12px;margin-top:5px;font-style:italic;font-weight:500;font-size:12px}
  .list-panel{position:absolute;top:235px;width:209px;padding:20px 0 0 30px;
    background:linear-gradient(180deg,rgba(25,25,25,.9),rgba(25,25,25,.55));font-weight:300;font-size:10.5px}
  .list-panel--installs{left:14px;height:300px;line-height:13.7px}
  .list-panel--offers{left:244px;height:150px;padding-left:17px;line-height:15.2px}
  .list-panel h3{font-weight:400;font-size:10.5px;margin-bottom:0;line-height:16px}
  .list-panel h3 span{color:var(--orange);font-weight:600;font-size:12px}
  .list-panel ul{list-style:none}
  .list-panel li::before{content:"- "}
</style>
</head>
<body>

<section class="page page--front">
  <div class="top-bar"></div>
  <div class="brand"><span class="brand__mark"></span><span class="brand__name">Mesa Ridge<br>Roofing</span></div>
  <div class="badge" role="img" aria-label="Certified contractor badge"></div>

  <div class="photo photo--facade" role="img" aria-label="Restaurant facade with green standing-seam metal roof"></div>
  <div class="photo photo--aerial" role="img" aria-label="Aerial view of a white flat commercial roof under construction"></div>
  <svg class="photo" style="left:0;top:83px" width="474" height="199" aria-hidden="true">
    <line x1="380" y1="6" x2="310" y2="199" stroke="#e8541f" stroke-width="1.5"/>
    <line x1="390" y1="6" x2="474" y2="6" stroke="#e8541f" stroke-width="1.5"/>
  </svg>
  <div class="accent-line" style="left:238px;top:96px;width:56px"></div>
  <div class="accent-line" style="left:305px;top:96px;width:16px"></div>
  <div class="accent-line" style="left:330px;top:96px;width:30px"></div>
  <p class="intro"><span class="hl">Mesa Ridge Roofing</span> opened the doors in 1984, and we’ve since installed, serviced, maintained, and coated <span class="hl">thousands of commercial roofs</span> around the state of Arizona, in the many climate regions of the state.</p>
  <div class="accent-line" style="left:177px;top:268px;width:43px"></div>
  <div class="accent-dash" style="left:240px;top:268px;width:63px"></div>

  <h2 class="specialty"><span class="outline">Our Specialty</span><br><span class="outline">Is </span><span class="solid">Commercial</span><br><span class="outline">Roofs</span></h2>
  <p class="body-text body-text--lead">Though we all live here for the constant sunshine, Arizona is one of the harshest environments in the US for roofs. Constant sun, heat, dryness, and then the torrential monsoon downpours</p>
  <p class="body-text body-text--call">All test the limits of your roof.</p>
  <p class="body-text body-text--small">We work with you to come up with a solution that works for your roof and will keep your business dry for years to come. Then, <span class="hl">our team of project managers, superintendents, foremen, and field workers</span> all come together to execute on that plan and <span class="hl">install a quality roof.</span></p>

  <div class="photo photo--store" role="img" aria-label="Coffee shop building with dark metal canopy and brick base"></div>
  <div class="store-bar"></div>

  <svg class="footer-shape" viewBox="0 0 474 73" preserveAspectRatio="none" aria-hidden="true">
    <path d="M284 2 H474 V73 H0 V32 H239 C258 32 264 2 284 2 Z" fill="#e8541f"/>
  </svg>
  <p class="phone">555 310 2290</p>
  <div class="contact"><p class="contact__licence">AZ ROC 512077</p><p>www.mesaridge-roofing.com</p><p>info@mesaridge-roofing.com</p></div>
</section>

<section class="page page--back">
  <div class="top-bar"></div>
  <div class="brand"><span class="brand__mark"></span><span class="brand__name">Mesa Ridge<br>Roofing</span></div>
  <div class="badge" role="img" aria-label="Certified contractor badge"></div>

  <div class="photo photo--backdrop" role="img" aria-label="Close view of a dark metal roof edge and parapet on a brick commercial building"></div>
  <div class="state-band"><p>We service the entire state of Arizona.</p></div>
  <div class="cert-band">
    <p>We are <strong>CERTIFIED</strong> with many different manufacturers, so we’re able to offer custom solutions to solve your issues, that will also often come with reputable manufacturer warranties.</p>
    <div class="makers"><span>Apexa</span><span>Summit</span><span>RB</span><span>Dura-Ply</span><span>Corvo</span><span>Pro-Seal</span><span>And more</span></div>
  </div>

  <div class="list-panel list-panel--installs">
    <h3>Mesa Ridge Roofing <span>INSTALLS</span></h3>
    <ul><li>TPO</li><li>PVC</li><li>Modified Bitumen</li><li>Silicone Coatings</li><li>Acrylic Coatings</li><li>Shingle</li><li>Metal</li><li>Tile</li><li>Spray Polyurethane Foam</li><li>And more</li></ul>
  </div>
  <div class="list-panel list-panel--offers">
    <h3>Mesa Ridge Roofing <span>OFFERS</span></h3>
    <ul><li>New Roof Installation</li><li>Re-roofing</li><li>Roof Maintenance and Service</li><li>Roof Inspections</li><li>Roof Coatings</li><li>And more</li></ul>
  </div>

  <svg class="footer-shape" viewBox="0 0 474 73" preserveAspectRatio="none" aria-hidden="true">
    <path d="M284 2 H474 V73 H0 V32 H239 C258 32 264 2 284 2 Z" fill="#e8541f"/>
    <path d="M0 26 H236 C256 26 262 -5 284 -5 H474" fill="none" stroke="#ffffff" stroke-width="1.5"/>
  </svg>
  <p class="phone">555 310 2290</p>
  <div class="contact"><p class="contact__licence">AZ ROC 512077</p><p>www.mesaridge-roofing.com</p><p>info@mesaridge-roofing.com</p></div>
</section>

</body>
</html>
```